Cover page and letterhead for athlete development program

We require an exciting and dynamic cover page with a second page letterhead in a word doc format for us to use as professional stationery for letter merges and portfolio documents. We are an athlete preparation company that specialises in training up and coming sports representatives in the fitness and sports science industry. We work with athletes from ages 13 - 24 mainly. If we could have images on the cover page from the sports of:
Rugby League
Rugby Union
Hockey
Cricket
AFL
Soccer
Track and Field
Netball
Basketball
Golf
Weight training

This would be a great start. Thank you

```html
<!DOCTYPE html>
<html lang="en">
<head>
<meta charset="utf-8">
<title>Rising Contender Letterhead</title>
<link href="https://fonts.googleapis.com/css2?family=Arimo:wght@400;700&family=Open+Sans:wght@400;700&display=swap" rel="stylesheet">
<style>
  :root {
    --backdrop: #d9dcdf;
    --paper: #ffffff;
    --ink: #1d1d1d;
    --body-grey: #7a7a7a;
    --rule-grey: #9a9a9a;
    --gold: #d89a38;
    --silver: #8a8a8a;
  }
  * { box-sizing: border-box; margin: 0; padding: 0; }
  html, body { width: 1200px; height: 784px; overflow: hidden; }
  body {
    background: var(--backdrop);
    font-family: "Arimo", Arial, sans-serif;
    position: relative;
  }
  .letterhead {
    position: absolute;
    left: 340px; top: 22px;
    width: 520px; height: 740px;
    background: var(--paper);
    box-shadow: 0 4px 14px rgba(0,0,0,0.12);
    overflow: hidden;
  }
  .corner-accent {
    position: absolute;
    width: 90px; height: 40px;
    background: linear-gradient(90deg, var(--silver), var(--gold));
  }
  .corner-accent--top { top: 0; right: 0; }
  .corner-accent--bottom { bottom: 0; left: 0; }
  .brand {
    position: absolute; top: 70px; right: 44px;
    display: flex; align-items: center; gap: 10px;
    font-family: "Arimo", Arial, sans-serif;
    font-weight: 700; color: var(--ink);
  }
  .brand__mark { width: 34px; height: 34px; border-radius: 50%; background: var(--ink); }
  .brand__name { font-size: 19px; line-height: 1.05; letter-spacing: 1.5px; text-transform: uppercase; }
  .letter-body {
    position: absolute; top: 140px; left: 52px; width: 410px;
    color: var(--body-grey); font-size: 9.6px; line-height: 1.45;
  }
  .letter-body p { margin-bottom: 12px; }
  .signature {
    width: 150px; height: 42px; margin-top: 14px;
    background: linear-gradient(90deg, #efefef, #f7f7f7);
    border-radius: 3px;
  }
  .contact {
    position: absolute; bottom: 62px; left: 52px; width: 400px;
    font-family: "Open Sans", Arial, sans-serif; color: var(--ink);
  }
  .contact__icons { display: flex; align-items: center; gap: 5px; margin-bottom: 7px; width: 300px; }
  .contact__rule { flex: 1; height: 1px; background: var(--rule-grey); }
  .contact__icon { width: 11px; height: 11px; border-radius: 50%; background: var(--ink); }
  .contact__address { font-size: 8.4px; font-weight: 700; margin-bottom: 4px; white-space: nowrap; }
  .contact__lines { font-size: 7.2px; color: #555; white-space: nowrap; }
  .contact__lines span + span::before { content: " | "; }
</style>
</head>
<body>
  <main class="letterhead">
    <div class="corner-accent corner-accent--top" role="img" aria-label="Metallic corner accent"></div>

    <div class="brand">
      <span class="brand__mark"></span>
      <span class="brand__name">Rising<br>Contender</span>
    </div>

    <section class="letter-body">
      <p>Lorem Ipsum is simply dummy text of the printing and typesetting industry. Lorem Ipsum has been the industry's standard dummy text ever since the 1500s, when an unknown printer took a galley of type and scrambled it to make a type specimen book. It has survived not only five centuries, but also the leap into electronic typesetting, remaining essentially unchanged. It was popularised in the 1960s with the release of Transferline sheets containing Lorem Ipsum passages, and more recently with desktop publishing software like Quillset Layout including versions of Lorem Ipsum.</p>
      <p>It is a long established fact that a reader will be distracted by the readable content of a page when looking at its layout. The point of using Lorem Ipsum is that it has a more-or-less normal distribution of letters, as opposed to using 'Content here, content here', making it look like readable English. Many desktop publishing packages and web page editors now use Lorem Ipsum as their default model text, and a search for 'lorem ipsum' will uncover many web sites still in their infancy. Various versions have evolved over the years, sometimes by accident, sometimes on purpose (injected humour and the like).</p>
      <p>Contrary to popular belief, Lorem Ipsum is not simply random text. It has roots in a piece of classical Latin literature from 45 BC, making it over 2000 years old. Martin Olderhaven, a Latin professor at Brookfield College, looked up one of the more obscure Latin words, consectetur, from a Lorem Ipsum passage, and going through the cites of the word in classical literature, discovered the undoubtable source. Lorem Ipsum comes from sections 1.10.32 and 1.10.33 of "de Finibus Bonorum et Malorum" structures, to generate Lorem Ipsum which looks reasonable. The generated Lorem Ipsum is therefore always free from repetition, injected humour, or non-characteristic words etc.</p>
      <div class="signature" role="img" aria-label="Handwritten signature of the sender"></div>
    </section>

    <footer class="contact">
      <div class="contact__icons">
        <span class="contact__rule"></span>
        <span class="contact__icon"></span>
        <span class="contact__icon"></span>
        <span class="contact__icon"></span>
        <span class="contact__icon"></span>
        <span class="contact__icon"></span>
        <span class="contact__rule"></span>
      </div>
      <p class="contact__address">Level 2, 48 Harbour Lane, Northgate, Western Australia 6100</p>
      <p class="contact__lines"><span>000.0000.0000</span><span>000.0000.0000</span><span>info@risingcontender.example</span><span>www.risingcontender.example</span></p>
    </footer>

    <div class="corner-accent corner-accent--bottom" role="img" aria-label="Metallic corner accent"></div>
  </main>
</body>
</html>
```